Bold Website Design for Fitness Trainer - No Coding

We are in need of a bold and unique website design for a personal fitness training company, www.TessaLorvel.com. We need DESIGN ONLY for three pages. These will be a homepage, a lead capture page, and one internal page with a sidebar. The design will be used for coding a wordpress theme, if that matters for the designer.

Tessa Lorvel Fitness Training
2738 E 19th St #415
Austin, TX 78705
512-607-4918
http://www.tessalorvel.com

Target Market(s)

18-45 year old male and females making 80k+ a year and looking to get stronger and in shape.

Industry/Entity Type

Fitness

Number of Pages Required

3 page

Font styles to use
Sans Serif

Requirements
Must have
• See attached design specs file.
Nice to have
Should not have
• Boxed layout.
• Dark Background.

```html
<!DOCTYPE html>
<html lang="en">
<head>
<meta charset="utf-8">
<title>Tessa Lorvel Fitness Training</title>
<link href="https://fonts.googleapis.com/css2?family=Montserrat:wght@400;700;800&family=Open+Sans:ital,wght@0,400;0,600;0,700;1,400;1,600&display=swap" rel="stylesheet">
<style>
:root{
  --pink:#e9318b;
  --cyan:#00b2ec;
  --ink:#111;
  --dark:#2f2f2f;
  --grey:#ececec;
  --card:#f4f4f4;
  --text:#555;
  --yellow:#f3e600;
  --white:#fff;
}
*{margin:0;padding:0;box-sizing:border-box}
html,body{width:1200px;height:1000px;overflow:hidden;background:var(--white)}
body{font-family:"Open Sans",Arial,sans-serif;color:var(--text);position:relative}
a{text-decoration:none}
.page{position:absolute;left:450px;top:0;width:300px;height:1000px;background:var(--white)}
.abs{position:absolute}
.head{font-family:"Montserrat",Arial,sans-serif;font-weight:800;text-transform:uppercase}

.topbar{left:0;top:0;width:300px;height:11px;background:var(--dark);color:var(--white);font-size:4.5px;font-weight:700;display:flex;align-items:center;padding-left:30px;gap:8px;white-space:nowrap}
.topbar span{display:flex;align-items:center;gap:2px}
.topbar .dot{width:4px;height:4px;border-radius:50%;background:var(--white);position:absolute;top:3.5px}

.brand{left:0;top:11px;width:300px;height:42px;display:flex;align-items:center;justify-content:center;gap:4px}
.brand-mark{width:22px;height:22px;border-radius:50%;background:var(--pink)}
.brand-name{font-family:"Montserrat",Arial,sans-serif;font-weight:800;font-size:11px;color:var(--ink);line-height:1}

.nav{left:0;top:53px;width:300px;height:11px;background:var(--pink);font-family:"Montserrat",Arial,sans-serif;font-size:4.4px;font-weight:700;color:var(--white);text-transform:uppercase;white-space:nowrap}
.nav a{position:absolute;top:0;height:11px;line-height:11px;color:inherit}
.nav .nav-free{left:225px;width:75px;text-align:center;background:var(--cyan)}

.hero{left:0;top:64px;width:300px;height:106px;background:radial-gradient(ellipse at 50% 55%,#6d6d6d 0%,#2a2a2a 55%,#0c0c0c 100%)}
.hero-title{left:0;top:127px;width:300px;text-align:center;color:var(--white);font-size:9px;font-weight:700}

.cta-blue{left:0;top:170px;width:300px;height:72px;background:var(--cyan);text-align:center}
.cta-blue h2{font-size:12px;color:var(--ink);margin-top:9px;line-height:16px}
.cta-blue .sub{font-family:"Montserrat",Arial,sans-serif;font-weight:800;font-size:7.5px;color:var(--white);line-height:10px}
.cta-blue .tags{font-size:4.2px;font-weight:700;color:#7fe0ff;letter-spacing:.3px;line-height:7px;text-transform:uppercase}
.btn{display:inline-block;background:var(--ink);color:var(--yellow);font-family:"Montserrat",Arial,sans-serif;font-weight:800;font-size:6px;line-height:8px;padding:2px 7px;text-transform:uppercase}
.cta-blue .btn{margin-top:3px}

.intro{left:45px;top:258px;width:210px;text-align:center;font-size:4.3px;line-height:7px}
.btn-outline{left:131px;top:293px;width:38px;height:9px;border:1px solid var(--ink);font-size:4.3px;font-weight:700;color:var(--ink);display:flex;align-items:center;justify-content:center;text-transform:uppercase}

.card{top:318px;width:78px;height:136px;background:var(--card);border-bottom:2px solid var(--pink);z-index:2}
.card h3{height:16px;background:var(--pink);color:var(--white);font-family:"Montserrat",Arial,sans-serif;font-size:4.5px;font-weight:700;display:flex;align-items:center;justify-content:center;text-transform:uppercase;white-space:nowrap}
.card .photo{width:60px;height:60px;border-radius:50%;margin:12px auto 0;background:radial-gradient(circle at 50% 40%,#cfcfcf,#7a7a7a 70%,#4a4a4a)}
.card p{font-size:3.6px;line-height:5.6px;text-align:center;padding:0 8px;margin-top:10px}

.reviews{left:0;top:448px;width:300px;height:90px;background:linear-gradient(90deg,#141414,#2e2e2e 50%,#141414)}
.reviews h2{position:absolute;left:0;top:17px;width:300px;text-align:center;font-family:"Montserrat",Arial,sans-serif;font-size:8px;font-weight:700;color:var(--pink)}
.reviews .avatar{left:57px;top:33px;width:34px;height:34px;border-radius:50%;background:radial-gradient(circle,#b8b8b8,#555);border:1.5px solid #ddd}
.reviews .quote{left:98px;top:37px;width:150px;font-size:4.3px;line-height:6.2px;font-style:italic;font-weight:600;color:var(--yellow)}
.reviews .who{left:54px;top:69px;width:40px;text-align:center;font-size:4px;font-style:italic;color:#bbb;white-space:nowrap}
.reviews svg{position:absolute;top:40px}

.follow{left:0;top:538px;width:300px;height:117px}
.follow h2{position:absolute;top:10px;width:300px;text-align:center;font-family:"Montserrat",Arial,sans-serif;font-size:9px;font-weight:700;color:var(--pink)}
.follow .label{font-family:"Montserrat",Arial,sans-serif;font-size:5.5px;font-weight:700;color:var(--ink);width:75px;white-space:nowrap}
.follow .shot{width:75px;height:75px;border:2px solid #555}
.shot-ig{background:linear-gradient(135deg,#8a7a6c,#c7b6a4 40%,#7b8ca3 70%,#5d4e46)}
.shot-fb{background:linear-gradient(180deg,#d9dbe4,#f4f4f4 40%,#b4b8c6)}

.posts{left:0;top:655px;width:300px;height:182px;background:var(--grey)}
.posts h2{position:absolute;top:10px;width:300px;text-align:center;font-family:"Montserrat",Arial,sans-serif;font-size:8px;font-weight:700;color:var(--pink)}
.post{left:28px;width:245px;height:37px}
.post .thumb{position:absolute;left:0;top:0;width:100px;height:36px;border-right:4px solid var(--cyan)}
.post h3{position:absolute;left:107px;top:0;font-size:5px;font-weight:700;color:var(--ink);white-space:nowrap}
.post p{position:absolute;left:107px;top:9px;width:135px;font-size:3.6px;line-height:5.2px}
.post .more{position:absolute;left:107px;top:30px;font-size:3.6px;font-weight:700;color:var(--ink)}

.cta-pink{left:0;top:837px;width:300px;height:80px;background:var(--pink);text-align:center}
.cta-pink h2{font-size:8.5px;color:var(--white);margin-top:14px;line-height:11px}
.cta-pink .tags{font-size:4.2px;font-weight:700;color:#f8bcd8;text-transform:uppercase;letter-spacing:.3px;line-height:6px}
.cta-pink .big{font-size:12.5px;color:var(--white);margin-top:4px;line-height:16px}
.cta-pink .btn{margin-top:4px}

.footer{left:28px;top:925px;width:245px;height:62px;display:flex;font-size:3.6px;line-height:5px;white-space:nowrap}
.footer .col{padding-right:6px}
.footer .col + .col{border-left:1px solid #e2e2e2;padding-left:6px}
.footer h4{font-size:3.8px;font-weight:700;color:var(--cyan);text-transform:uppercase;margin-top:3px}
.footer .phone{font-size:7px;color:#444;line-height:9px}
.icons{display:flex;gap:5px;margin-top:5px}
.icons i{width:5px;height:5px;border-radius:50%;display:block}

.bottombar{left:0;top:990px;width:300px;height:10px;background:var(--dark);color:#ccc;font-size:3.4px;display:flex;align-items:center;justify-content:center;white-space:nowrap}
</style>
</head>
<body>
<div class="page">

  <div class="abs topbar">
    <span><svg width="4" height="5" viewBox="0 0 4 5"><path d="M.5 .5h1l.5 1.2-.6.5a3 3 0 0 0 1 1l.5-.6 1.1.5v1H3A3 3 0 0 1 .5 1.5z" fill="#e9318b"/></svg>(512) 607-4918</span>
    <span><svg width="4" height="5" viewBox="0 0 4 5"><path d="M2 5 .4 2.4A1.6 1.6 0 1 1 3.6 2.4z" fill="#e9318b"/></svg>LOCATION</span>
    <span><svg width="4" height="4" viewBox="0 0 4 4"><rect width="4" height="4" fill="#e9318b"/></svg>CALENDAR</span>
    <i class="dot" style="left:235px"></i><i class="dot" style="left:241px"></i><i class="dot" style="left:247px"></i><i class="dot" style="left:253px"></i>
  </div>

  <div class="abs brand">
    <span class="brand-mark"></span>
    <span class="brand-name">Tessa Lorvel</span>
  </div>

  <nav class="abs nav">
    <a href="#" style="left:37px">Home</a>
    <a href="#" style="left:64px">Programs</a>
    <a href="#" style="left:102px">Meet Your Trainer</a>
    <a href="#" style="left:162px">Blog</a>
    <a href="#" style="left:187px">Contact Me</a>
    <a href="#" class="nav-free">Free Session!</a>
  </nav>

  <div class="abs hero" role="img" aria-label="Black and white photo of hands gripping a barbell"></div>
  <div class="abs hero-title head">Austin's #1 Personal Trainer</div>

  <section class="abs cta-blue">
    <h2 class="head">Get Started Today!</h2>
    <div class="sub">Your First Session is FREE!</div>
    <div class="tags">General Fitness • Weight Loss • Strength Training • Powerlifting</div>
    <a class="btn" href="#">Sign Up Now »</a>
  </section>

  <p class="abs intro">IronPath is constantly varied, functional movements executed at high intensity.<br>Our program gives you a more balanced overall fitness, increasing your capability and capacity over a broader range of movements and activities. And what we do is scalable to accommodate different levels of experience, injury or other limiting factors.</p>
  <a class="abs btn-outline" href="#">Read More</a>

  <div class="abs card" style="left:28px">
    <h3>1-on-1 Personal Training</h3>
    <div class="photo" role="img" aria-label="Photo of a client training on a cable machine"></div>
    <p>Tessa specializes in personal training conducting Weight Loss and Nutrition programs in addition to strength training sessions &amp; Boot Camps.</p>
  </div>
  <div class="abs card" style="left:111px">
    <h3>Online Coaching</h3>
    <div class="photo" role="img" aria-label="Photo of an athlete squatting with a barbell"></div>
    <p>We will capture your individual fitness goals and provide the tools and training necessary to achieve them.</p>
  </div>
  <div class="abs card" style="left:194px">
    <h3>Strength Programming</h3>
    <div class="photo" role="img" aria-label="Photo of an athlete lifting a barbell"></div>
    <p>A proper program can provide significant functional benefits and improvement in overall health and well-being.</p>
  </div>

  <section class="abs reviews" role="group" aria-label="Client testimonials">
    <h2>Words from my Clients</h2>
    <div class="abs avatar" role="img" aria-label="Client portrait"></div>
    <p class="abs quote">Tessa's training methods are addictive and will leave you wanting more after every workout. Every day has new challenging workouts and it's impossible to get bored with it. Whether you're a fitness pro for years or just starting out, it's a great environment and an even better community to join. Delighted to recommend!</p>
    <div class="abs who">Dalen Ross</div>
    <svg style="left:31px" width="6" height="14" viewBox="0 0 6 14"><path d="M5 1 1 7l4 6" stroke="#777" fill="none"/></svg>
    <svg style="left:265px" width="6" height="14" viewBox="0 0 6 14"><path d="M1 1l4 6-4 6" stroke="#777" fill="none"/></svg>
  </section>

  <section class="abs follow">
    <h2>Follow Me</h2>
    <div class="abs label" style="left:51px;top:20px">Photo Feed</div>
    <div class="abs shot shot-ig" style="left:51px;top:28px" role="img" aria-label="Grid of recent training photos"></div>
    <div class="abs label" style="left:175px;top:20px;text-align:right">Social Page</div>
    <div class="abs shot shot-fb" style="left:175px;top:28px" role="img" aria-label="Preview of the social page feed"></div>
  </section>

  <section class="abs posts">
    <h2>Latest Posts</h2>
    <article class="abs post" style="top:31px">
      <div class="thumb" role="img" aria-label="Photo of a woman training in the gym" style="background:linear-gradient(90deg,#2b3d55,#5c7aa0 50%,#1d2533)"></div>
      <h3>Chest, Shoulders, Triceps and Back</h3>
      <p>15 Rest/Pause – You have 3 sets to get a total of 15 reps with the same weight. In the first set your goal is to hit at least 8 reps, 2nd set 4 reps and 3rd set at least 3 reps. If you can do more than 15 now, then the weight is too light.</p>
      <span class="more">more »</span>
    </article>
    <article class="abs post" style="top:81px">
      <div class="thumb" role="img" aria-label="Photo of a bench press session" style="background:linear-gradient(90deg,#1c1c1c,#6a6a6a 50%,#2a2a2a)"></div>
      <h3>Training Legs and Biceps</h3>
      <p>You want to go as heavy as you can for each set without losing form, so make sure the weight is suitable for you. You also want to go at least parallel, below is even better (ATG), and make sure you have the proper footwear as well.</p>
      <span class="more">more »</span>
    </article>
    <article class="abs post" style="top:131px">
      <div class="thumb" role="img" aria-label="Photo of an overhead barbell lift" style="background:linear-gradient(90deg,#202020,#5a5a5a 50%,#161616)"></div>
      <h3>What Motivates Me To Be Healthy and Stay Fit</h3>
      <p>People often ask me, "What keeps you going?" or "How do you stay motivated?" For me it is really the fact that I cherish being healthy and I love working out. Our bodies were NOT meant to sit on couches staring at glowing screens.</p>
      <span class="more">more »</span>
    </article>
  </section>

  <section class="abs cta-pink">
    <h2 class="head">Schedule Your Free Session</h2>
    <div class="tags">General Fitness • Weight Loss • Strength Training • Powerlifting</div>
    <div class="big head">Sign Up Now!</div>
    <a class="btn" href="#">Get Started »</a>
  </section>

  <footer class="abs footer">
    <div class="col" style="width:80px">
      <h4>Call</h4>
      <div class="phone">(512) 607-4918</div>
      <h4 style="margin-top:6px">Address</h4>
      <div>Tessa Lorvel Fitness Training<br>2738 E 19th St #415<br>Austin, TX 78705</div>
    </div>
    <div class="col" style="width:88px">
      <h4>Resources</h4>
      <div style="display:flex;gap:6px">
        <div>› IronPath<br>› IronPath Endure<br>› Interval Daily<br>› Row Club<br>› Gym Skills<br>› IronPath Gym</div>
        <div>› Lift Talk<br>› Capital Fit<br>› Movement<br>› The Steady Way<br>› Mobility Lab</div>
      </div>
    </div>
    <div class="col" style="width:77px">
      <h4>Connect With Me</h4>
      <div class="icons"><i style="background:#3b5998"></i><i style="background:#2fa8e0"></i><i style="background:#d34836"></i><i style="background:#c4302b"></i><i style="background:#cb2027"></i><i style="background:#b35a3a;border-radius:1px"></i></div>
    </div>
  </footer>

  <div class="abs bottombar">Copyright © 2015 · Tessa Lorvel Fitness Training · (512) 607-4918 · Privacy Policy · Terms of Use</div>

</div>
</body>
</html>
```